Dental Practice Billboard Design

We are a newer dental practice in need of a simple but appealing billboard for our growing dental practice to attract new patients. The practice is owned by husband and wife dentists and is family friendly in a small town in Kentucky. We try to be very friendly and caring to our patients. Would prefer a blue background for the billboard and our tooth logo to be prominent. We are partial to the Patua One font used in the image below but please feel free to tweak it as you deem necessary. The shape of the uppercase D and lowercase g are why we like that font, so fonts with a similarly shaped “D” and “g” would work as well. Please include our phone number (606) 847-3962. Please see our website Harlowfamilydentistry.com for more info on the practice if needed. Thank you! Looking forward to seeing your creation.
Updates

The dimensions will be 12ft x 24ft (3.6576m x 7.3152m). Apologies for not including this in the original prompt. Thank you all for your submissions.

Industry/Entity Type

Dental

Font styles to use
Other font styles liked:
• Patua One

Colors
0054AA
0677BA
7BADD7
CADEEF
E8F1F8
0094D4
00A9DD
6FCCEA
C7EBF8
E9F6FB
00AB8E
00BBA5
67D7C9
C6EFE9
E9F9F6
59FF00
82FF00
B8FF75
E3FFCB
F4FFEA

Requirements
Must have
• Phone number, website, Logo, Practice name “Harlow Family Dentistry”
Should not have
• A tagline or slogan

```html
<!DOCTYPE html>
<html lang="en">
<head>
<meta charset="utf-8">
<title>Harlow Family Dentistry – Billboard</title>
<link rel="stylesheet" href="https://fonts.googleapis.com/css2?family=Patua+One&display=swap">
<style>
  :root {
    --page-bg: #e8f1f8;
    --board-top: #1d4fa6;
    --board-bottom: #123f92;
    --brand-white: #ffffff;
    --text-light: #e8f1f8;
    --text-soft: #cadeef;
    --accent-sky: #6fccea;
    --accent-cyan: #00a9dd;
    --tree-dark: #0f2f73;
  }
  * { margin: 0; padding: 0; box-sizing: border-box; }
  html, body {
    width: 1200px;
    height: 1000px;
    overflow: hidden;
    background: var(--page-bg);
  }
  .canvas {
    width: 1200px;
    height: 1000px;
    display: flex;
    align-items: center;
    justify-content: center;
  }
  .billboard {
    position: relative;
    width: 1120px;
    height: 560px;
    background: linear-gradient(180deg, var(--board-top) 0%, var(--board-bottom) 100%);
    overflow: hidden;
    font-family: "Patua One", Georgia, serif;
  }
  .brand {
    position: absolute;
    left: 150px;
    top: 88px;
    display: flex;
    align-items: center;
    gap: 34px;
  }
  .brand-mark {
    width: 170px;
    height: 170px;
    border-radius: 50%;
    background: var(--brand-white);
    flex-shrink: 0;
  }
  .brand-text { display: flex; flex-direction: column; }
  .brand-name {
    color: var(--brand-white);
    font-weight: 400;
    font-size: 112px;
    line-height: 1;
    letter-spacing: 1px;
  }
  .brand-sub {
    color: var(--brand-white);
    font-size: 52px;
    line-height: 1.05;
    margin-left: 4px;
  }
  .contact {
    position: absolute;
    left: 395px;
    top: 305px;
    display: flex;
    flex-direction: column;
    gap: 16px;
  }
  .contact-row { display: flex; align-items: center; gap: 26px; }
  .contact-icon { width: 40px; height: 40px; flex-shrink: 0; }
  .phone-number {
    color: var(--text-soft);
    font-size: 64px;
    line-height: 1;
  }
  .website {
    color: var(--text-light);
    font-size: 38px;
    line-height: 1;
  }
  .treeline-area {
    position: absolute;
    right: 0;
    top: 300px;
    width: 460px;
    height: 170px;
    background: linear-gradient(90deg, rgba(15,47,115,0) 0%, rgba(15,47,115,0.55) 45%, rgba(15,47,115,0.8) 100%);
  }
  .wave-band {
    position: absolute;
    left: 0;
    bottom: 40px;
    width: 1120px;
    height: 60px;
    background: linear-gradient(180deg, rgba(111,204,234,0) 0%, rgba(0,169,221,0.35) 50%, rgba(111,204,234,0) 100%);
  }
</style>
</head>
<body>
<main class="canvas">
  <section class="billboard" aria-label="Harlow Family Dentistry billboard">
    <div class="treeline-area" role="img" aria-label="Pine tree line silhouette"></div>
    <div class="wave-band" role="img" aria-label="Flowing blue wave lines"></div>

    <div class="brand">
      <div class="brand-mark" aria-hidden="true"></div>
      <div class="brand-text">
        <h1 class="brand-name">Harlow</h1>
        <p class="brand-sub">Family Dentistry</p>
      </div>
    </div>

    <div class="contact">
      <div class="contact-row">
        <svg class="contact-icon" viewBox="0 0 24 24" aria-hidden="true">
          <path fill="var(--text-light)" d="M6.6 10.8a15.1 15.1 0 0 0 6.6 6.6l2.2-2.2a1 1 0 0 1 1-.25 11.4 11.4 0 0 0 3.6.57 1 1 0 0 1 1 1V20a1 1 0 0 1-1 1A17 17 0 0 1 3 4a1 1 0 0 1 1-1h3.5a1 1 0 0 1 1 1c0 1.25.2 2.45.57 3.57a1 1 0 0 1-.25 1z"/>
        </svg>
        <p class="phone-number">(606) 847-3962</p>
      </div>
      <div class="contact-row">
        <svg class="contact-icon" viewBox="0 0 24 24" aria-hidden="true">
          <g fill="none" stroke="var(--text-light)" stroke-width="1.6">
            <circle cx="12" cy="12" r="9.5"/>
            <ellipse cx="12" cy="12" rx="4.2" ry="9.5"/>
            <line x1="2.5" y1="12" x2="21.5" y2="12"/>
            <line x1="4" y1="7" x2="20" y2="7"/>
            <line x1="4" y1="17" x2="20" y2="17"/>
          </g>
        </svg>
        <p class="website">harlowfamilydentistry.com</p>
      </div>
    </div>
  </section>
</main>
</body>
</html>
```